BM PowerPoint Template Refresh

I'm looking to refresh our corporate presentation collateral, namely our base PowerPoint template. I need something that sparks, and gives the appearance of our contemporary firm that is hip, innovative, and modern. The project should provide for the various slide master templates with appropriately sized background images for slides in 4:3 and 16:9 formats

Target Market(s)

Investment banking prospect and clients which are typically in the high-tech industries of software, semiconductors,telecom, and telecom components

Industry/Entity Type

Investment Banking

Font styles to use
Other font styles liked:
• Goudy Old Style

Requirements
Must have
• - Must leverage current logo (red color is the standard, however portions of the logo or, color variations from our stock are possible for use), primary and secondary current colors. Non-section text is Goudy Old Style (headers and body text)
- The PPT template must have at least all of the LAYOUT options found in the Old BM Prez
- Options with and without the Brecon logo as a transparent background
- Need a final version in 16:9 and 4:3 formats
- Must be able to add footer information such as "Confidential Information", slide number, and date
Nice to have
• a few design ideas on the IP Engineering image found on slide 7 of the New BM Prez Attempt.ppt file

```html
<!DOCTYPE html>
<html lang="en">
<head>
<meta charset="utf-8">
<title>Brecon Advisors Overview</title>
<link href="https://fonts.googleapis.com/css2?family=Sorts+Mill+Goudy&display=swap" rel="stylesheet">
<style>
  :root {
    --band-red: #ff3515;
    --band-rose: #e03a55;
    --band-plum: #8a4f8c;
    --band-blue: #3a60a6;
    --ink: #1e1e1e;
    --white: #ffffff;
    --photo-dark: #2e3136;
    --photo-mid: #4c5259;
    --photo-light: #c9ccd0;
  }
  html, body { margin: 0; padding: 0; overflow: hidden; background: var(--white); }
  .slide {
    position: relative; width: 1200px; height: 675px; overflow: hidden;
    background: var(--white);
    font-family: "Sorts Mill Goudy", "Goudy Old Style", Georgia, serif;
    color: var(--ink);
  }
  .title-band {
    position: absolute; left: 0; top: 0; width: 1200px; height: 98px;
    background: linear-gradient(90deg, var(--band-red) 0%, var(--band-rose) 35%, var(--band-plum) 68%, var(--band-blue) 100%);
  }
  .slide-title {
    position: absolute; left: 49px; top: 33px; margin: 0;
    font-size: 23px; font-weight: normal; color: var(--white); line-height: 32px;
  }
  .overview {
    position: absolute; left: 0; top: 118px; width: 720px;
    margin: 0; padding: 0; list-style: none;
    font-size: 15px; line-height: 21.5px;
  }
  .overview li { position: relative; margin-bottom: 11.5px; }
  .point { padding-left: 71px; }
  .point::before {
    content: ""; position: absolute; left: 51px; top: 8px;
    width: 5px; height: 5px; background: var(--ink);
  }
  .sub { padding-left: 138px; }
  .sub::before {
    content: "o"; position: absolute; left: 94px; top: 0;
  }
  b { font-weight: bold; }
  .feature-photo {
    position: absolute; left: 758px; top: 143px; width: 442px; height: 440px;
    background: radial-gradient(circle at 45% 50%, var(--photo-mid) 0%, var(--photo-dark) 60%),
                linear-gradient(160deg, var(--photo-dark), var(--photo-light));
  }
</style>
</head>
<body>
<div class="slide">
  <header class="title-band">
    <h1 class="slide-title">Brecon Advisors Overview</h1>
  </header>

  <ul class="overview">
    <li class="point">A leading financial advisory firm for the middle market serving companies that:</li>
    <li class="sub">Possess niche <b>intellectual property</b> and/or product/service experiences</li>
    <li class="sub">Have created value by specializing and offering <b>unique products or services</b></li>
    <li class="point">Our team of Operational Deal Makers leverages decades of experience owning, operating, and advising <b>middle market companies</b> and management board</li>
    <li class="sub">We partner with our clients to identify growth partners possessing debt and equity capital and strategic or synergistic offerings</li>
    <li class="point">Our points of differentiation:</li>
    <li class="sub">Involve two ‘senior’&nbsp; partners with <b>solid business &amp; financial network</b> actively on each deal from start to closing</li>
    <li class="sub">Relatively Strong technical + business <b>operations &amp; deal experience in Tech</b> including understanding&nbsp; <b>emerging tech value chain</b></li>
    <li class="sub"><b>Quantify strategic synergies</b>, value prop, Unlock value of <b>Patents &amp; IP and</b> overall <b>business ROI</b> a lot better</li>
    <li class="sub"><b>Motivate Corp/BU sponsors</b> well before warming the corp dev to lock value where it matters the most</li>
    <li class="sub">Deliver <b>best in class IM</b> that becomes an 'asset' and most often <b>cuts the closure time</b>/DD by half. Broad industry, operational and financial experience</li>
  </ul>

  <div class="feature-photo" role="img" aria-label="Photo of a hand holding a smartphone over notes, overlaid with glowing business and technology icons"></div>
</div>
</body>
</html>
```